Business Card with Multiple Logos

We are looking for a simple and elegant card covering all our brand Logos (VELIN, MealTrove, Pelrina, VELIN Express) and showing what all we do (Restaurants, Catering, Import & Distribution, Information Technology). The name of the company is "TORVIK Ventures" which we prefrably want as EMBOSS. The information should be easy to read. Incase required, i am open for a foldable card. I am also interested to use recycled paper.
Updates
+ An Overview / Background of the Business & ServicesWe are into Import & Distribution, Restaurants, Catering | Concept Retail Store & IT services. All these services represent their parent company Sharing the common group name e.g. TORVIK Logistics, TORVIK Supermart, TORVIK Hospitality, etc. And the main (Share Holding Company name is TORVIK Ventures) For the key management people. I am looking for a concept that "TORVIK Ventures" whould be mentioned on the card and inside either we show all the sub division company names, and/or their Brand Logos+ The Target Market / Audience you are trying to reachBusiness Associates+ Design Specifics; any preferences or ideas for Style, Colour, Imagery, etcIt should be classy, but sober at the same time. Although we have Orange as a color theme but I am open to explore something new as well. + Contact information to be included in the cardsBusiness Address (Lane 47, Ratchada Soi 9, Opp. B L Fenwood Hotel, Banrakphi, Bangkok 10480 Thailand)Contact Details T : +662 739 5162 | F : +662 739 5163 | W : www.torvik.example | E : pn@torvik.example Added Friday, March 27, 2015
Industry/Entity Type
Business
Contact Information for Business Card
Name : Anil Prabhakar
Designation : Group Director
Address : Lane 47, Ratchada Soi 9, Banrakphi, Bangkok 10480 Thailand (Landmark : Opp. B L Fenwood Hotel)
Email : pn@torvik.example | M : +66857206134 | W : www.torvik.example
Contact : O : +662 739 5162 | F : +662 739 5163
Requirements
Must have
- Our Brand Logos (4 in number)

```html
<!DOCTYPE html>
<html lang="en">
<head>
<meta charset="utf-8">
<title>TORVIK Ventures — Business Card</title>
<link href="https://fonts.googleapis.com/css2?family=Open+Sans:ital,wght@0,400;0,600;0,700;1,400;1,700&display=swap" rel="stylesheet">
<style>
  :root {
    --orange: #f05a28;
    --navy: #0d4a80;
    --card-white: #ffffff;
    --card-grey: #e4e5e7;
    --backdrop: #ecebe8;
    --ink-light: #ffffff;
  }
  * { margin: 0; padding: 0; box-sizing: border-box; }
  html, body {
    width: 1200px;
    height: 900px;
    overflow: hidden;
    background: var(--backdrop);
    font-family: "Open Sans", Arial, sans-serif;
  }
  .canvas { position: relative; width: 1200px; height: 900px; }
  .card {
    position: absolute;
    left: 290px;
    width: 620px;
    height: 354px;
    border-radius: 22px;
    overflow: hidden;
    box-shadow: 0 10px 28px rgba(0,0,0,0.18);
  }
  .card--front {
    top: 70px;
    background: radial-gradient(ellipse at 45% 40%, var(--card-white) 40%, #efeff0 100%);
  }
  .card--back {
    top: 476px;
    background: linear-gradient(160deg, var(--card-white) 20%, var(--card-grey) 90%);
  }
  .wordmark {
    display: flex;
    align-items: center;
    gap: 10px;
    color: var(--orange);
    font-weight: 600;
    letter-spacing: 0.5px;
    white-space: nowrap;
  }
  .wordmark__square { width: 14px; height: 14px; background: var(--navy); }
  .front-stack {
    position: absolute;
    left: 0; right: 0; top: 50%;
    transform: translateY(-50%);
    display: flex;
    flex-direction: column;
    align-items: center;
    gap: 34px;
  }
  .wordmark--group { font-size: 40px; }
  .brands { display: flex; gap: 24px; }
  .wordmark--brand { font-size: 17px; gap: 7px; }
  .wordmark--brand .wordmark__square { width: 9px; height: 9px; }
  .card--back .wordmark--lead {
    position: absolute;
    left: 130px;
    top: 48px;
    font-size: 44px;
  }
  .card__swoosh { position: absolute; inset: 0; width: 100%; height: 100%; }
  .holder {
    position: absolute;
    left: 32px;
    top: 262px;
    color: var(--ink-light);
  }
  .holder__name { font-size: 21px; font-weight: 700; font-style: italic; line-height: 1.2; }
  .holder__title { font-size: 18px; font-style: italic; font-weight: 400; line-height: 1.2; }
  .contact {
    position: absolute;
    left: 362px;
    top: 224px;
    list-style: none;
    color: var(--ink-light);
    font-size: 11.5px;
    line-height: 14.5px;
  }
  .contact__item { display: flex; align-items: flex-start; gap: 7px; margin-bottom: 3px; }
  .contact__icon { flex: 0 0 12px; width: 12px; height: 12px; margin-top: 1px; }
</style>
</head>
<body>
<main class="canvas">

  <section class="card card--front" aria-label="Card front">
    <div class="front-stack">
      <div class="wordmark wordmark--group">
        <span class="wordmark__square" aria-hidden="true"></span>
        <span>TORVIK Ventures</span>
      </div>
      <div class="brands">
        <div class="wordmark wordmark--brand"><span class="wordmark__square" aria-hidden="true"></span><span>VELIN</span></div>
        <div class="wordmark wordmark--brand"><span class="wordmark__square" aria-hidden="true"></span><span>MealTrove</span></div>
        <div class="wordmark wordmark--brand"><span class="wordmark__square" aria-hidden="true"></span><span>Pelrina</span></div>
        <div class="wordmark wordmark--brand"><span class="wordmark__square" aria-hidden="true"></span><span>VELIN Express</span></div>
      </div>
    </div>
  </section>

  <section class="card card--back" aria-label="Card back">
    <svg class="card__swoosh" viewBox="0 0 620 354" preserveAspectRatio="none" aria-hidden="true">
      <path d="M0,176 Q290,294 620,74 Q300,302 0,194 Z" fill="var(--navy)"/>
      <path d="M0,202 Q300,312 620,82 L620,354 L0,354 Z" fill="var(--orange)"/>
    </svg>

    <div class="wordmark wordmark--lead">
      <span class="wordmark__square" aria-hidden="true"></span>
      <span>VELIN Express</span>
    </div>

    <div class="holder">
      <p class="holder__name">Anil Prabhakar</p>
      <p class="holder__title">Group Director</p>
    </div>

    <ul class="contact">
      <li class="contact__item">
        <svg class="contact__icon" viewBox="0 0 14 14" aria-hidden="true"><circle cx="7" cy="7" r="7" fill="#fff"/><path d="M3.5,7.5 L7,4 L10.5,7.5 M4.8,7 V10.3 H9.2 V7" fill="none" stroke="var(--orange)" stroke-width="1.3"/></svg>
        <span>Lane 47, Ratchada Soi 9,<br>Opp. B L Fenwood Hotel, Banrakphi,<br>Bangkok 10480 Thailand</span>
      </li>
      <li class="contact__item">
        <svg class="contact__icon" viewBox="0 0 14 14" aria-hidden="true"><circle cx="7" cy="7" r="7" fill="#fff"/><path d="M4.5,3.5 Q3.5,8 9.5,10.5 L10.3,9 L8.7,8 L7.8,8.8 Q5.8,7.6 5.4,6 L6.2,5.2 L5.4,3.5 Z" fill="var(--orange)"/></svg>
        <span>O : +662 739 5162 | F : +662 739 5163</span>
      </li>
      <li class="contact__item">
        <svg class="contact__icon" viewBox="0 0 14 14" aria-hidden="true"><circle cx="7" cy="7" r="7" fill="#fff"/><rect x="4.8" y="3" width="4.4" height="8" rx="0.8" fill="var(--orange)"/></svg>
        <span>M : +66857206134</span>
      </li>
      <li class="contact__item">
        <svg class="contact__icon" viewBox="0 0 14 14" aria-hidden="true"><circle cx="7" cy="7" r="7" fill="#fff"/><rect x="3.5" y="4.5" width="7" height="5" fill="var(--orange)"/><path d="M3.5,4.5 L7,7.5 L10.5,4.5" fill="none" stroke="#fff" stroke-width="0.9"/></svg>
        <span>pn@torvik.example</span>
      </li>
      <li class="contact__item">
        <svg class="contact__icon" viewBox="0 0 14 14" aria-hidden="true"><circle cx="7" cy="7" r="7" fill="#fff"/><circle cx="7" cy="7" r="3.8" fill="none" stroke="var(--orange)" stroke-width="1"/><path d="M3.2,7 H10.8 M7,3.2 V10.8" stroke="var(--orange)" stroke-width="0.9"/></svg>
        <span>www.torvik.example</span>
      </li>
    </ul>
  </section>

</main>
</body>
</html>
```